Premium Lawn fertiliser packaging - Looking for long term designer

*Update at bottom
I need a carefully considered, bold and professional packaging design for my new premium lawn fertiliser product. This contest is for a detailed front of the stand-up pouch packaging and once I’ve chosen a winner, they’ll be asked to create the layout for the back that links to the front as well. I have a full range of additional products that will also need designs and so I'm looking for someone who can do a great job here and who we can work with long term.

The front should include our logo for Brindley Turf Supply Direct and be titled “Meadow Rise Max” "Professional Lawn Fertiliser". The spring fertiliser tag line is "Awaken your lawn: Lush Greening, Lasting Health".
Beneath it, it then needs to include some important usage information and the key benefits along with some suitable graphic.

Key information to include:

Apply March - June
Treats 35-50 m2
16-3-8
+2%MgO + 1% Fe + 2.9% CaO (this is the chemical makeup of the fertiliser and needs to be fairly prominent. If you look at other professional fertiliser packaging, you'll see how it needs to compare).

Key features:
Premium fertiliser, used by professionals
Advanced greening with micro-nutrient complex
Dual action Nitrogen: Instant green boost & continuous feed for 3 months
Child & pet safe

Our brand colours are purple and green. Purple = #592999, Green = 3cb64a / 81d742 / 4d9d44

I think these colours look great against a white background.

Please make sure you look at our website as well to get an idea of our brand: www.brindleyturfsupply.co.uk

To help, I've attached images of competitors fertiliser packaging that I like the look of. I'm not looking for you to copy but just see what type of thing appeals to me, the standard I'm expecting and what I need to compete against....

In addition, I have also attached some potential images you may wish to try using in your design, although please feel free to use your own if you have something better. For the moment, the images are 'preview' images, but once I decide on a design and we agree on the correct image, I will download and send over a fully licensed version.

*** Update*** When submitting your design, can you submit it in 2 formats: The first as a fully printed custom stand-up pouch and the second as a full-size label stuck onto a standup pouch (whatever colour you think is right for your design - choose white if you are not sure). To explain, I've just discovered we won't be able to get full custom bags printed in time for the first run and so we will have to opt for the design to be printed on labels and fixed onto bags. I therefore need to choose a design that works in both formats as both a label on a standup pouch as well as a fully printed pouch. Many thanks.

Target Market(s)

Domestic home-owners

Industry/Entity Type

Lawn care. NOT AGRICULTURE OR FARMING

Font styles to use
Sans Serif

Requirements
Must have
• Presented in 2 formats - see update at bottom of description
Nice to have
• I quite like designs against a white background, although I’m open to other ideas as well.
Should not have
• Please do not include any people or faces in the design. The text should be solid in colour, so no graduated colour fill in the text or outline text. Please avoid over-busy or cluttered designs.

```html
<!DOCTYPE html>
<html lang="en">
<head>
<meta charset="utf-8">
<title>Meadow Rise Max – Professional Lawn Fertiliser</title>
<link href="https://fonts.googleapis.com/css2?family=Arimo:wght@400;700&family=Chicle&display=swap" rel="stylesheet">
<style>
  :root {
    --page: #6f4a8f;
    --brand-purple: #592999;
    --deep-purple: #3b0f73;
    --badge-purple: #4a1894;
    --brand-green: #81d742;
    --tag-green: #5f9a2e;
    --tag-green-dark: #4d8a2a;
    --lime-text: #8cc43a;
    --band-black: #101010;
    --white: #ffffff;
    --soft-white: #ececec;
    --field-orange: #e98b4f;
  }
  * { box-sizing: border-box; margin: 0; padding: 0; }
  html, body { width: 1200px; height: 972px; overflow: hidden; }
  body {
    background: var(--page);
    font-family: "Arimo", Arial, sans-serif;
    position: relative;
  }
  .pouch {
    position: absolute;
    left: 317px; top: 27px;
    width: 566px; height: 918px;
    overflow: hidden;
    background: var(--brand-purple);
  }
  .hero-photo {
    position: absolute; left: 0; top: 0; width: 566px; height: 555px;
    background: linear-gradient(180deg, #5e2fa8 0%, #6a3aa6 40%, #7a4c9c 62%, #a2708a 80%, #b98070 100%);
  }
  .lawn-photo {
    position: absolute; left: 0; top: 697px; width: 566px; height: 221px;
    background: linear-gradient(180deg, #4e8f22 0%, #3f7a1c 45%, #2f5e16 100%);
  }
  .apply-tag { position: absolute; left: 35px; top: 0; width: 144px; height: 152px; }
  .apply-tag svg { position: absolute; inset: 0; }
  .apply-icon {
    position: absolute; left: 44px; top: 22px; width: 56px; height: 50px;
    background: linear-gradient(180deg, #d9a47a 0%, var(--field-orange) 100%);
    border-radius: 4px;
  }
  .apply-label {
    position: absolute; left: 0; width: 144px; top: 70px; text-align: center; color: var(--white);
  }
  .apply-label .word { font-size: 17px; font-weight: 700; line-height: 18px; display: block; }
  .apply-label .months { font-size: 12.5px; font-weight: 700; line-height: 15px; display: block; }
  .brand {
    position: absolute; left: 210px; top: 18px; width: 190px; text-align: center; color: var(--white);
    font-weight: 400;
  }
  .brand-dot {
    width: 34px; height: 34px; border-radius: 50%; background: var(--brand-green);
    margin: 0 auto 10px;
  }
  .brand-name { font-size: 28px; line-height: 30px; display: block; }
  .brand-sub { font-size: 10.5px; letter-spacing: 2.4px; line-height: 14px; display: block; }
  .product-title {
    position: absolute; left: 0; width: 566px; top: 150px;
    font-family: "Chicle", "Arimo", sans-serif; color: var(--white);
    text-align: center; text-transform: uppercase;
  }
  .product-title span { display: block; padding-left: 24px; }
  .title-line-1 { font-size: 118px; line-height: 98px; letter-spacing: 2px; }
  .title-line-2 { font-size: 140px; line-height: 116px; letter-spacing: 3px; }
  .title-line-3 { font-size: 236px; line-height: 190px; letter-spacing: 6px; }
  .product-band {
    position: absolute; left: 0; top: 555px; width: 566px; height: 64px;
    background: var(--band-black); text-align: center;
  }
  .product-type { color: var(--lime-text); font-size: 26.5px; font-weight: 700; line-height: 30px; margin-top: 8px; letter-spacing: 0.3px; }
  .tagline { color: var(--white); font-size: 15px; font-weight: 700; line-height: 18px; }
  .green-rule { position: absolute; left: 0; top: 619px; width: 566px; height: 8px; background: linear-gradient(180deg, #6db43a, #3e8a2c); }
  .usage-band {
    position: absolute; left: 0; top: 627px; width: 566px; height: 70px;
    background: rgba(89, 41, 153, 0.82); text-align: center; color: var(--soft-white);
  }
  .coverage { font-size: 18px; font-weight: 700; margin-top: 12px; line-height: 22px; }
  .analysis { font-size: 15.5px; margin-top: 5px; line-height: 19px; }
  .benefit {
    position: absolute; top: 764px; width: 117px; height: 117px; border-radius: 50%;
    border: 4px solid var(--white);
    background: radial-gradient(circle at 40% 35%, var(--badge-purple), var(--deep-purple));
    color: var(--white); font-weight: 700; text-align: center;
    display: flex; flex-direction: column; align-items: center; justify-content: center;
    box-shadow: 0 3px 6px rgba(0,0,0,0.35);
    font-size: 11.5px; line-height: 15px; text-transform: uppercase;
  }
  .benefit small { font-size: 7.6px; font-weight: 400; line-height: 11px; display: block; padding: 0 8px; }
  .benefit.large { font-size: 17px; line-height: 24px; }
  .benefit-1 { left: 40px; }
  .benefit-2 { left: 165px; }
  .benefit-3 { left: 294px; }
  .benefit-4 { left: 422px; }
</style>
</head>
<body>
  <main class="pouch">
    <div class="hero-photo" role="img" aria-label="Close-up of lawn grass blades in a purple wash fading into a warm sunset field"></div>
    <div class="lawn-photo" role="img" aria-label="Lush green lawn stretching to the horizon"></div>

    <div class="apply-tag">
      <svg width="144" height="152" viewBox="0 0 144 152" aria-hidden="true">
        <defs>
          <linearGradient id="tagFill" x1="0" y1="0" x2="0" y2="1">
            <stop offset="0" stop-color="#6fa331"/>
            <stop offset="1" stop-color="#4d8a2a"/>
          </linearGradient>
        </defs>
        <polygon points="0,0 144,0 144,108 72,152 0,108" fill="url(#tagFill)"/>
        <polyline points="6,0 6,104 72,144 138,104 138,0" fill="none" stroke="#d9efc0" stroke-width="1" stroke-dasharray="2 2"/>
      </svg>
      <div class="apply-icon" role="img" aria-label="Seed packet scattering seed onto soil with sprouts"></div>
      <p class="apply-label"><span class="word">APPLY</span><span class="months">March - June</span></p>
    </div>

    <div class="brand">
      <div class="brand-dot"></div>
      <span class="brand-name">Brindley</span>
      <span class="brand-sub">TURF SUPPLY DIRECT</span>
    </div>

    <h1 class="product-title">
      <span class="title-line-1">Meadow</span>
      <span class="title-line-2">Rise</span>
      <span class="title-line-3">Max</span>
    </h1>

    <section class="product-band">
      <p class="product-type">PROFESSIONAL LAWN FERTILISER</p>
      <p class="tagline">Awaken your lawn: Lush Greening, Lasting Health</p>
    </section>
    <div class="green-rule"></div>

    <section class="usage-band">
      <p class="coverage">TREATS 35-50 M2</p>
      <p class="analysis">16-3-8 +2%MgO + 1% Fe + 2.9% CaO</p>
    </section>

    <div class="benefit benefit-1">Premium<br>fertiliser<br>used by<br>professionals</div>
    <div class="benefit benefit-2">Advanced<br>greening with<br>micro-nutrient<br>complex</div>
    <div class="benefit benefit-3">Dual action<br>nitrogen:<small>INSTANT GREEN BOOST &amp; CONTINUOUS FEED FOR 3 MONTHS</small></div>
    <div class="benefit benefit-4 large">Child &amp;<br>pet safe</div>
  </main>
</body>
</html>
```